Turfwisp.com needs a professional yet bold design to share our differences and convert customers!

We need web design for the only company to offer same day & next day lawn care services to the North Carolina Piedmont Triad area! Customers will be able to view cost and book their lawn service in 5 minutes via our website. We need to promote the following that set us apart: 1: No Contract 2: Instant Scheduling 3: Same Day Service 4: Fully Licensed and Insured, 5: Money Back Guarantee. We are the ONLY company in the area to offer this service.
The site needs to be bold to show the reasons we are different. "in your face", yet professional enough to earn a customer's trust. Inspiration can be drawn from sites such as broomsquadry.com, however the creative piece will be up to you to create a website that is perhaps unique, slightly tacky, different, etc. The key is for it to be the BEST in the area and easy to use without confusing customers. Must be able to allure customers in and have an easy checkout and booking procedure.
Updates

Reason: Request by some designers. Plan to make decision before this Friday.

Target Market(s)

People that want a simple, quick, and easy way to get someone to mow their grass!

Industry/Entity Type

It Company

Logo Text

Turf Wisp logo design opportunity to be offered as well.

Number of Pages Required

1 page

Requirements
Must have
• simple, bold, yet instill trust from the public.
Nice to have
• Need chat now, book now, popups showing % off that day. Need Zip code entry to price lawns. Need it to emphasize the quick process, reliability of the company, etc.

```html
<!DOCTYPE html>
<html lang="en">
<head>
<meta charset="utf-8">
<title>Verdantline – Lawn Care</title>
<link href="https://fonts.googleapis.com/css2?family=Open+Sans:ital,wght@0,400;0,600;0,700;1,400&display=swap" rel="stylesheet">
<style>
:root{
  --ink:#333333;
  --ink-soft:#555555;
  --line:#3a3a3a;
  --panel:#ececec;
  --band:#eeeeee;
  --white:#ffffff;
  --dark:#2b2b2b;
  --footer:#262626;
  --hero-a:#1c2a17;
  --hero-b:#34502a;
  --press:#9a9a9a;
  --play:rgba(20,20,20,.55);
}
*{box-sizing:border-box;margin:0;padding:0}
html,body{width:1200px;height:2394px;overflow:hidden;background:var(--white)}
body{font-family:"Open Sans",Arial,sans-serif;color:var(--ink);position:relative}

/* header */
.site-header{position:absolute;left:0;top:0;width:1200px;height:109px;background:var(--white)}
.brand{position:absolute;left:99px;top:30px;display:flex;align-items:center;gap:12px}
.brand-dot{width:34px;height:34px;border-radius:50%;background:var(--ink)}
.brand-name{font-size:32px;font-weight:400;color:var(--ink);letter-spacing:.5px}
.main-nav{position:absolute;right:100px;top:54px;display:flex;gap:36px;font-size:13.5px;color:#8c8c8c}
.main-nav .active{color:var(--ink);font-weight:600}

/* hero */
.hero{position:absolute;left:0;top:109px;width:1200px;height:454px;background:linear-gradient(180deg,var(--hero-a) 0%,#2a4121 45%,var(--hero-b) 100%)}
.hero-copy{position:absolute;left:163px;top:112px;width:420px;color:var(--white)}
.hero-copy h1{font-size:22px;line-height:32px;font-weight:700;text-transform:uppercase;letter-spacing:.3px}
.hero-copy p{margin-top:4px;font-size:12px;line-height:20.5px;color:#e6e6e6}
.btn-light{display:inline-block;margin-top:16px;background:var(--white);color:var(--ink);font-size:14px;padding:0;height:48px;line-height:48px;width:113px;text-align:center}
.hero-video{position:absolute;left:652px;top:114px;width:384px;height:227px;border:3px solid var(--white);background:linear-gradient(135deg,#3d5a2c,#8a7a55 60%,#b79f6e)}
.play{position:absolute;left:162px;top:83px;width:54px;height:54px;border-radius:50%;background:var(--play);border:2px solid rgba(255,255,255,.8)}
.play:after{content:"";position:absolute;left:19px;top:14px;border-left:18px solid var(--white);border-top:11px solid transparent;border-bottom:11px solid transparent}
.slide-arrow{position:absolute;top:210px;width:26px;height:34px;background:rgba(0,0,0,.35)}
.slide-arrow.left{left:0}.slide-arrow.right{right:0}

/* zip */
.zip-band{position:absolute;left:0;top:563px;width:1200px;height:163px;background:var(--band);text-align:center}
.zip-band h2{margin-top:38px;font-size:21px;font-weight:700;color:var(--ink-soft);letter-spacing:.3px}
.zip-form{position:absolute;left:415px;top:77px;display:flex}
.zip-input{width:278px;height:47px;background:var(--white);border:1px solid #dddddd;font-size:13px;color:#aaaaaa;text-align:left;padding:14px 18px}
.zip-next{width:89px;height:47px;background:var(--dark);color:var(--white);font-weight:700;font-size:16px;line-height:47px}

/* info columns */
.info-col{position:absolute;top:772px;width:309px}
.info-col h3{font-size:21px;font-weight:700;color:var(--ink);height:38px;border-bottom:5px solid var(--line);letter-spacing:.2px;position:relative}
.info-box{background:var(--panel);height:258px;position:relative}
.col-1{left:100px}.col-2{left:447px}.col-3{left:791px}
.col-2 h3{text-align:center}.col-3 h3{text-align:right}
.chev{position:absolute;right:0;top:6px}
.avatar{position:absolute;left:26px;top:20px;width:82px;height:82px;border-radius:50%;background:radial-gradient(circle,#c9a98a,#8a6f5a);border:3px solid var(--white)}
.reviewer{position:absolute;left:126px;top:52px;font-size:13.5px;color:var(--ink-soft)}
.quote{position:absolute;left:28px;top:136px;width:262px;font-size:13px;line-height:22px;font-style:italic;color:var(--ink-soft);text-indent:34px}
.qmark{position:absolute;font-family:Georgia,"Times New Roman",serif;font-size:48px;font-weight:700;font-style:normal;color:var(--ink);line-height:1;text-indent:0}
.q-open{left:0;top:-4px}
.q-close{left:252px;top:198px}
.secure-badge{position:absolute;left:54px;top:36px;width:200px;height:190px;background:linear-gradient(180deg,#e2e2e2,#d6d6d6);border-radius:4px}
.hours{position:absolute;left:27px;top:24px;font-size:13px;color:var(--ink-soft);line-height:20px}
.hours b{display:block;font-size:15px;font-weight:600;color:var(--ink)}
.hours .gap{margin-top:16px}
.hours a{display:block;margin-top:12px;color:var(--ink);font-weight:600;font-size:15px;text-decoration:underline}
.listing-badge{margin-top:14px;width:97px;height:23px;border:2px solid #c8332c;border-radius:4px;background:#fbe2e0}

.divider{position:absolute;left:100px;top:1119px;width:1000px;height:1px;background:#d8d8d8}

/* why */
.why{position:absolute;left:0;top:1178px;width:1200px;text-align:center}
.why h2{font-size:30px;font-weight:700;color:var(--ink)}
.why p{margin:16px auto 0;width:870px;font-size:12.5px;line-height:21px;color:var(--ink-soft)}
.feature{position:absolute;width:340px}
.feature h4{display:flex;align-items:center;gap:10px;font-size:24px;font-weight:600;color:var(--ink);margin-left:-32px;white-space:nowrap}
.feature h4 svg{flex:none}
.feature p{margin-top:8px;font-size:11px;line-height:17.5px;color:var(--ink-soft)}
.f1{left:202px;top:1352px}.f2{left:700px;top:1352px}
.f3{left:202px;top:1515px}.f4{left:700px;top:1515px}
.f5{left:452px;top:1678px}

/* press */
.press{position:absolute;left:0;top:1848px;width:1200px;height:224px;background:var(--band);text-align:center}
.press .label{margin-top:39px;font-size:15px;color:var(--ink-soft)}
.press-row{display:flex;justify-content:center;align-items:center;gap:38px;margin-top:20px;color:var(--press);font-size:24px;font-weight:600}
.press-row + .press-row{margin-top:28px}

/* cta */
.cta{position:absolute;left:0;top:2118px;width:1200px;text-align:center}
.cta h2{font-size:29px;font-weight:400;color:var(--ink)}
.cta p{margin-top:2px;font-size:13px;color:var(--ink-soft)}
.btn-dark{display:inline-block;margin-top:12px;width:146px;height:40px;line-height:40px;background:var(--dark);color:var(--white);font-size:15px;font-weight:700}

/* footer */
.site-footer{position:absolute;left:0;top:2290px;width:1200px;height:104px;background:var(--footer);color:#9a9a9a}
.foot-nav{position:absolute;left:100px;top:28px;font-size:11.5px}
.foot-nav span{padding:0 8px;color:#666}
.copyright{position:absolute;left:100px;top:57px;font-size:11px}
.social{position:absolute;left:832px;top:40px;display:flex;gap:10px}
.social i{display:block;width:24px;height:24px;border-radius:50%}
</style>
</head>
<body>

<header class="site-header">
  <div class="brand"><span class="brand-dot"></span><span class="brand-name">Verdantline</span></div>
  <nav class="main-nav">
    <span class="active">Landscape Projects</span><span>About</span><span>Design</span><span>Installation</span><span>Maintenance</span><span>Contact</span>
  </nav>
</header>

<section class="hero" role="img" aria-label="Photo of a manicured garden with clipped hedges and lawn">
  <span class="slide-arrow left"></span><span class="slide-arrow right"></span>
  <div class="hero-copy">
    <h1>Phasellus nisl est, condimentum vitae faucibus in, sollicitudin vel metus consequat.</h1>
    <p>Donec molestie nisi et tellus hendrerit vehicula. Nunc eu ligula sed quam pulvinar maximus in vitae eros. Proin porta fermentum ipsum, vel porttitor turpis venenatis luctus. Vivamus volutpat eu sapien quis tempus.</p>
    <span class="btn-light">Book Now</span>
  </div>
  <div class="hero-video" role="img" aria-label="Video still of a garden patio with lounge chairs">
    <span class="play"></span>
  </div>
</section>

<section class="zip-band">
  <h2>AENEAN FAUCIBUS LACUS UT MOLLIS COMMODO</h2>
  <div class="zip-form"><div class="zip-input">Zip code</div><div class="zip-next">NEXT</div></div>
</section>

<section class="info-col col-1">
  <h3>HAPPY CUSTOMERS
    <svg class="chev" width="14" height="18" viewBox="0 0 14 18"><path d="M3 2l8 7-8 7" fill="none" stroke="#333" stroke-width="2"/></svg>
  </h3>
  <div class="info-box">
    <span class="avatar" role="img" aria-label="Customer portrait"></span>
    <span class="reviewer">Dale Morrow</span>
    <p class="quote"><span class="qmark q-open">&ldquo;</span>Nullam accumsan purus vel tempus viverra. Mauris suscipit felis nunc elemen tum varius. Praesent elementum nulla sit amet justo pellentesque scelerisque.</p>
    <span class="qmark q-close">&rdquo;</span>
  </div>
</section>

<section class="info-col col-2">
  <h3>TRUSTWORTHY &amp; SECURE</h3>
  <div class="info-box">
    <span class="secure-badge" role="img" aria-label="Secure checkout badge with padlock and accepted payment cards"></span>
  </div>
</section>

<section class="info-col col-3">
  <h3>HOURS AND LOCATIONS</h3>
  <div class="info-box">
    <div class="hours">
      <b>Hours of operation :</b>MonSun: 8:30 AM 5:00 PM
      <b class="gap">Find our location :</b>22 Building name, Street name<br>City - Zipcode
      <a>View More Service Areas</a>
      <div class="listing-badge" role="img" aria-label="Review listing badge"></div>
    </div>
  </div>
</section>

<div class="divider"></div>

<section class="why">
  <h2>Why Verdantline?</h2>
  <p>Nam et tortor in ante iaculis porttitor in luctus mi. Vivamus gravida sem a pretium euismod. Nam lobortis, purus et fringilla tempus, risus eros dignissim diam, eget finibus sem risus sit amet eros. Vestibulum facilisis dolor at purus tincidunt porta. Nam fringilla nulla vel nisl condimentum, dapibus condimentum enim porta.</p>
</section>

<div class="feature f1">
  <h4><svg width="20" height="20" viewBox="0 0 20 20"><rect x="1" y="4" width="14" height="14" fill="none" stroke="#333" stroke-width="2"/><path d="M8 12l9-9 2 2-9 9H8z" fill="#333"/></svg>No Contract</h4>
  <p>Nam tempus, quam in bibendum vulputate, sapien dolor viverra nisl, vitae euismod elit turpis et nulla. Aliquam erat volutpat. Pellentesque blandit lacus eget nunc faucibus.</p>
</div>
<div class="feature f2">
  <h4><svg width="20" height="20" viewBox="0 0 20 20"><rect x="1" y="3" width="18" height="16" fill="none" stroke="#333" stroke-width="2"/><rect x="1" y="3" width="18" height="4" fill="#333"/><path d="M5 10h2M9 10h2M13 10h2M5 14h2M9 14h2M13 14h2" stroke="#333" stroke-width="2"/></svg>Instant Scheduling</h4>
  <p>Nam tempus, quam in bibendum vulputate, sapien dolor viverra nisl, vitae euismod elit turpis et nulla. Aliquam erat volutpat. Pellentesque blandit lacus eget nunc faucibus.</p>
</div>
<div class="feature f3">
  <h4><svg width="20" height="20" viewBox="0 0 20 20"><path d="M2 18C2 8 8 3 19 2 18 13 12 18 4 16z" fill="#333"/></svg>Same Day Service</h4>
  <p>Nam tempus, quam in bibendum vulputate, sapien dolor viverra nisl, vitae euismod elit turpis et nulla. Aliquam erat volutpat. Pellentesque blandit lacus eget nunc faucibus.</p>
</div>
<div class="feature f4">
  <h4><svg width="20" height="20" viewBox="0 0 20 20"><rect x="1" y="8" width="4" height="10" fill="#333"/><path d="M7 8l4-7c2 0 2 2 1 5h6c1 0 2 1 1 3l-2 8H7z" fill="#333"/></svg>Fully Licensed and Insured,</h4>
  <p>Nam tempus, quam in bibendum vulputate, sapien dolor viverra nisl, vitae euismod elit turpis et nulla. Aliquam erat volutpat. Pellentesque blandit lacus eget nunc faucibus.</p>
</div>
<div class="feature f5">
  <h4><svg width="22" height="16" viewBox="0 0 22 16"><rect x="1" y="1" width="20" height="14" fill="none" stroke="#333" stroke-width="2"/><circle cx="11" cy="8" r="3.5" fill="#333"/></svg>Money Back Guarantee.</h4>
  <p>Nam tempus, quam in bibendum vulputate, sapien dolor viverra nisl, vitae euismod elit turpis et nulla. Aliquam erat volutpat. Pellentesque blandit lacus eget nunc faucibus.</p>
</div>

<section class="press">
  <div class="label">As Featured In</div>
  <div class="press-row"><span>Daybook</span><span>Ledgerly</span><span>TradeWeekly</span><span>Quick Firm</span><span>The Capitol Herald</span></div>
  <div class="press-row"><span>SportLine</span><span>Fit Living</span><span>Finer Points</span><span>Game Pages</span></div>
</section>

<section class="cta">
  <h2>Proin a dolor mauris</h2>
  <p>Aliquam nunc mauris, vestibulum id justo eget molestie rutrum dolor molestie nisi.</p>
  <span class="btn-dark">BOOK NOW</span>
</section>

<footer class="site-footer">
  <div class="foot-nav">Landscape Projects<span>|</span>About<span>|</span>Design<span>|</span>Installation<span>|</span>Maintenance<span>|</span>Contact</div>
  <div class="copyright">Copyright &nbsp;©&nbsp; 2015 &nbsp;Verdantline. &nbsp;All rights reserved.</div>
  <div class="social" aria-label="Social links">
    <i style="background:#3b5998"></i><i style="background:#1da1f2"></i><i style="background:#555"></i><i style="background:#cb2027"></i><i style="background:#f57d00"></i><i style="background:#c4302b"></i><i style="background:#2a6aa8"></i><i style="background:#5aa843"></i>
  </div>
</footer>

</body>
</html>
```